Re designing of website of VELTARO Pens, an International stationary brand

We would like to re design our existing website veltaropens.com. We are leading manufacturers and exporters of stationary products. Our existence is global -selling and marketing in all 5 continents.

We are a 35year old group with focus on high quality, innovative designs and state of art manufacturing setup.

Client satisfaction by committed service and trust are the roots of our organisation.

We would like to see a website which focuses on our brand Veltaro and must have an international appeal. Our target buyers would be Agents, distributors and wholesalers in various countries. Content would be similar to our existing website but designing and outlook needs to be totally different.

For the outlook we do like the following websites from our industry which can be used to draw inspiration.
1. www.quillbrookstationery.example
2. www.marovipen.example
3. www.tulsbergpen.example

The homepage need not be focused on the product but must emphasis on the branding of Veltaro, our existence of 35years along with international presence and quality standards maintained by our organisation.
Updates

Reason: Would like to see some more concepts and designs as per artwork attached.

Target Market(s)

Wholesalers, Agents and Distributors in all countries around the world. Target market is global

Number of Pages Required

1 page

Font styles to use
Sans Serif

Requirements
Must have
• Focus on Branding, High Quality Standards, Customer Loyalty
Nice to have
• Like the outlook of the websites
• www.tulsbergpen.example
• www.quillbrookstationery.example
• www.marovipen.example
Should not have
• Don't like the outlook of our present website www.veltaropens.com
• It doesn't justify our brand or our product

```html
<!DOCTYPE html>
<html lang="en">
<head>
<meta charset="utf-8">
<title>VELTARO – World Class Writing Instruments</title>
<link href="https://fonts.googleapis.com/css2?family=PT+Sans:wght@400;700&display=swap" rel="stylesheet">
<style>
:root{
  --red:#e3121a;
  --red-dark:#b8141b;
  --red-card:#d4232c;
  --ink:#3a3a3a;
  --muted:#7a7a7a;
  --band:#ebebeb;
  --panel:#f2f2f2;
  --footer:#2a2627;
  --footer-text:#a9a5a5;
  --white:#ffffff;
}
*{box-sizing:border-box;margin:0;padding:0}
html,body{width:1048px;height:1200px;overflow:hidden}
body{font-family:"PT Sans",sans-serif;background:var(--white);position:relative;color:var(--ink)}

.site-header{position:absolute;left:0;top:0;width:1048px;height:69px;background:linear-gradient(#f3111a,#d9141b)}
.brand{position:absolute;left:82px;top:15px;display:flex;align-items:center;gap:7px;color:var(--white)}
.brand-mark{width:31px;height:31px;background:var(--white)}
.brand-name{font-size:28px;font-weight:400;line-height:1;letter-spacing:.5px}
.brand-tag{position:absolute;left:39px;top:29px;font-size:8px;white-space:nowrap}
.main-nav{position:absolute;left:311px;top:18px;display:flex;align-items:center;height:36px}
.main-nav a{color:var(--white);text-decoration:none;font-size:14px;padding:0 14px;line-height:36px}
.main-nav a.active{background:#151515;border-radius:3px;padding:0 17px;margin-right:1px}

.hero{position:absolute;left:0;top:69px;width:1048px;height:416px;
  background:radial-gradient(ellipse at 50% 10%,#79d5f5 0%,#6fa6c4 35%,#6b6f94 70%,#5a4f7a 100%)}
.hero-title{position:absolute;left:0;width:100%;top:118px;text-align:center;color:var(--white);
  font-size:53px;font-weight:700;letter-spacing:.5px;text-shadow:3px 4px 0 rgba(0,0,0,.3)}
.hero-sub{position:absolute;left:0;width:100%;top:191px;text-align:center;color:var(--white);font-size:17px}
.hero-btn{position:absolute;left:438px;top:237px;width:172px;height:60px;border-radius:3px;
  background:linear-gradient(#e5161e,#c2141b);color:var(--white);font-size:18px;font-weight:700;
  display:flex;align-items:center;justify-content:center}
.hero-dots{position:absolute;left:502px;top:375px;display:flex;gap:11px}
.hero-dots span{width:7px;height:7px;border-radius:50%;background:#8a8a9a}
.hero-dots span.on{background:#cfcfd8}

.feature-band{position:absolute;left:0;top:485px;width:1048px;height:257px;background:var(--band)}
.feature-card{position:absolute;top:36px;width:283px;height:188px;background:var(--white);padding:11px;
  box-shadow:0 1px 3px rgba(0,0,0,.12)}
.feature-photo{width:100%;height:165px;position:relative;overflow:hidden;background:linear-gradient(#8c7a66,#b49c80)}
.feature-label{position:absolute;left:0;bottom:0;width:100%;height:50px;background:var(--red-card);opacity:.95;
  color:var(--white);font-size:18px;font-weight:700;padding:15px 13px;text-shadow:1px 1px 0 rgba(0,0,0,.25)}

.welcome{position:absolute;left:86px;top:780px;width:605px}
.welcome h1{font-size:27px;font-weight:700;color:var(--ink);line-height:1}
.welcome h1 span{color:var(--red-dark)}
.welcome p{font-size:11.5px;line-height:18.3px;color:var(--muted);margin-top:26px}
.welcome p+p{margin-top:18px}
.read-more{position:absolute;left:0;top:225px;width:94px;height:41px;border-radius:3px;
  background:linear-gradient(#e0161e,#c0141b);color:var(--white);font-size:12px;display:flex;align-items:center;justify-content:center}

.products-panel{position:absolute;left:717px;top:764px;width:244px;height:319px;background:var(--panel);border-radius:3px}
.products-head{height:74px;background:linear-gradient(#ea1219,#c8141b);border-radius:3px 3px 0 0;color:var(--white);
  font-size:27px;font-weight:700;padding:20px 23px;text-shadow:1px 1px 0 rgba(0,0,0,.2)}
.products-list{list-style:none;padding:14px 0 0 24px}
.products-list li{font-size:11.5px;color:#555;line-height:23.3px;display:flex;align-items:center;gap:10px}
.products-list li::before{content:"›";color:#888;font-size:11px}

.site-footer{position:absolute;left:0;top:1116px;width:1048px;height:84px;background:var(--footer)}
.footer-links{position:absolute;left:86px;top:21px;font-size:11.5px;color:var(--footer-text)}
.footer-links span{margin:0 6px}
.copyright{position:absolute;left:86px;top:40px;font-size:11.5px;color:var(--footer-text)}
.social{position:absolute;left:802px;top:22px;display:flex;gap:6px}
.social span{width:27px;height:27px;background:#3d3839}
</style>
</head>
<body>

<header class="site-header">
  <div class="brand">
    <div class="brand-mark"></div>
    <div class="brand-name">VELTARO</div>
    <div class="brand-tag">World Class Writing Instruments</div>
  </div>
  <nav class="main-nav">
    <a class="active">Home</a>
    <a>About</a>
    <a>Retail Products</a>
    <a>Promotional Products</a>
    <a>Careers</a>
    <a>Enquiry Form</a>
    <a>Contact Us</a>
  </nav>
</header>

<section class="hero" role="img" aria-label="Desk flat-lay of notebooks, pencils, rulers, clipboard and notepads on a blue-purple gradient">
  <h2 class="hero-title">OFFICE STATIONERY</h2>
  <p class="hero-sub">Ball Pens, Gel Pens, Metal Pens, Art Material, Notebooks, Refills, Packaging, POP</p>
  <div class="hero-btn">VIEW PRODUCTS</div>
  <div class="hero-dots"><span></span><span class="on"></span><span></span></div>
</section>

<section class="feature-band">
  <div class="feature-card" style="left:86px">
    <div class="feature-photo" role="img" aria-label="Wooden desk with laptop, phone and office supplies" style="background:linear-gradient(#6e6358,#a89276)">
      <div class="feature-label">RETAIL PRODUCTS</div>
    </div>
  </div>
  <div class="feature-card" style="left:383px">
    <div class="feature-photo" role="img" aria-label="Colored pencils in a cup beside a stack of notebooks" style="background:linear-gradient(#5c4a3e,#9c8670)">
      <div class="feature-label">PROMOTIONAL PRODUCTS</div>
    </div>
  </div>
  <div class="feature-card" style="left:681px">
    <div class="feature-photo" role="img" aria-label="Paints, colored pencils and paper clips on a wooden table" style="background:linear-gradient(#a88f6e,#c9b08c)">
      <div class="feature-label">CATALOGUE</div>
    </div>
  </div>
</section>

<section class="welcome">
  <h1>WELCOME TO <span>VELTARO</span></h1>
  <p>Veltaro is one of India's largest manufacturers and exporters of writing instruments. Established in 1976, Veltaro has witnessed phenomenal growth over the last many years and now boast of customers across various segments in markets across the globe.</p>
  <p>Our commitment to developing new and original designs, creating innovative finishes and emphasis on complete customer satisfaction have been major catalysts of our steady progress as we continue to expand business across North America, South America, Europe, Africa, Asia and Australia. Our range of writing products also caters very successfully to the ever increasing needs of the domestic Indian market.</p>
  <div class="read-more">READ MORE</div>
</section>

<aside class="products-panel">
  <div class="products-head">PRODUCTS</div>
  <ul class="products-list">
    <li>Ball Pens</li>
    <li>Gel Pens</li>
    <li>Metal Pens</li>
    <li>Art Material</li>
    <li>Office Stationery</li>
    <li>Notebooks</li>
    <li>Refills</li>
    <li>Packaging</li>
    <li>POP</li>
  </ul>
</aside>

<footer class="site-footer">
  <div class="footer-links">Home<span>/</span>Retail Products<span>/</span>Promotional Products<span>/</span>Careers<span>/</span>Enquiry Form<span>/</span>Contact Us</div>
  <div class="copyright">Copyright © 2015</div>
  <div class="social"><span></span><span></span><span></span><span></span><span></span></div>
</footer>

</body>
</html>
```